Wine Label for a Prosecco Wine Called Vuro

Prosecco is a white sparkling wine from Italy. We are looking for an eye catching, elegant label for this prosecco that is called "Vuro" because it is a young, fresh, lively white sparkling wine. (We do not want to see children or babies featured on the label-- just the name VURO please.) Attached is the old label for your reference, and the bottle type that will be used , which is a dark green Burgundy style bottle (pls ignore the label on the bottle). Please no grapes or wine glasses on the label. We are looking for something: eye catching / fun / ELEGANT (not cheap). We would be happy with a fun color too. Remember-- elegant, eye catching! Thanks!
Updates

Hi All, I think I made a mistake in my brief and have updated it. I also uploaded a competitor's label that we like very much to give better direction to what we are looking for. Also, the word Vuro cannot be vertical, nor can it be broken. It needs to read: VURO or Vuro. Thanks

Target Market(s)

American adults male and female.

Colors
abd036
33a6d7
33b8a4
ffcf3e

Requirements
Must have
• The mandatory information as shown on old labels. The word VURO should be very prominent.
Nice to have
• The uploaded photo of a competitor's prosecco shows a label we really like... if you could play around with this shape and style we'd be very happy.
Should not have
• No grape images, no wine glass images, no images of babies or children.

```html
<!DOCTYPE html>
<html lang="it">
<head>
<meta charset="utf-8">
<title>Vuro Prosecco – Label Variants</title>
<link rel="stylesheet" href="https://fonts.googleapis.com/css2?family=Montserrat:wght@400;500;700;800&family=Allura&display=swap">
<style>
  :root {
    --bg: #e2e2e2;
    --teal: #33b8a4;
    --blue: #33a6d7;
    --yellow: #ffcf3e;
    --lime: #abd036;
    --white: #ffffff;
    --ink: #0a0a0a;
  }
  * { margin: 0; padding: 0; box-sizing: border-box; }
  html, body {
    width: 1200px;
    height: 927px;
    overflow: hidden;
    background: var(--bg);
  }
  .board {
    position: relative;
    width: 1200px;
    height: 927px;
    display: grid;
    grid-template-columns: 229px 229px;
    grid-template-rows: 365px 365px;
    column-gap: 28px;
    row-gap: 23px;
    justify-content: center;
    align-content: center;
  }
  .label {
    position: relative;
    width: 229px;
    height: 365px;
    font-family: "Montserrat", sans-serif;
    text-align: center;
  }
  .label--teal { background: var(--teal); }
  .label--blue { background: var(--blue); }

  .label__mark {
    position: absolute;
    left: 61px;
    top: 47px;
    width: 111px;
    height: 110px;
    background: linear-gradient(135deg, #ffffff 0%, #fbfbf2 45%, #f3f8ea 100%);
  }
  .label__name {
    position: absolute;
    left: 0;
    right: 0;
    top: 176px;
    font-weight: 800;
    font-size: 61px;
    line-height: 1;
    letter-spacing: 1px;
    color: var(--white);
  }
  .label--dark-name .label__name { color: var(--ink); }
  .label__type {
    position: absolute;
    left: 0;
    right: 0;
    top: 222px;
    padding-right: 6px;
    font-family: "Allura", cursive;
    font-size: 40px;
    line-height: 1;
    color: var(--yellow);
  }
  .label__region {
    position: absolute;
    left: 0;
    right: 0;
    top: 278px;
    font-weight: 700;
    font-size: 17px;
    letter-spacing: 1.5px;
    line-height: 1;
    color: var(--white);
  }
  .label__igt {
    position: absolute;
    left: 0;
    right: 0;
    top: 314px;
    font-weight: 500;
    font-size: 8.4px;
    letter-spacing: 0.3px;
    line-height: 1;
    color: var(--yellow);
  }
  .label__style {
    position: absolute;
    left: 0;
    right: 0;
    top: 338px;
    font-weight: 400;
    font-size: 8px;
    letter-spacing: 0.6px;
    line-height: 1;
    color: var(--white);
  }
</style>
</head>
<body>
<main class="board">

  <article class="label label--teal">
    <div class="label__mark" role="img" aria-label="Square emblem of crossing diagonal lines in blue, yellow, lime and teal"></div>
    <h2 class="label__name">VURO</h2>
    <p class="label__type">Prosecco</p>
    <p class="label__region">VENETO</p>
    <p class="label__igt">INDICAZIONE GEOGRAFICA TIPICA</p>
    <p class="label__style">FRIZZANTE</p>
  </article>

  <article class="label label--blue">
    <div class="label__mark" role="img" aria-label="Square emblem of crossing diagonal lines in blue, yellow, lime and teal"></div>
    <h2 class="label__name">VURO</h2>
    <p class="label__type">Prosecco</p>
    <p class="label__region">VENETO</p>
    <p class="label__igt">INDICAZIONE GEOGRAFICA TIPICA</p>
    <p class="label__style">FRIZZANTE</p>
  </article>

  <article class="label label--teal label--dark-name">
    <div class="label__mark" role="img" aria-label="Square emblem of crossing diagonal lines in blue, yellow, lime and teal"></div>
    <h2 class="label__name">VURO</h2>
    <p class="label__type">Prosecco</p>
    <p class="label__region">VENETO</p>
    <p class="label__igt">INDICAZIONE GEOGRAFICA TIPICA</p>
    <p class="label__style">FRIZZANTE</p>
  </article>

  <article class="label label--blue label--dark-name">
    <div class="label__mark" role="img" aria-label="Square emblem of crossing diagonal lines in blue, yellow, lime and teal"></div>
    <h2 class="label__name">VURO</h2>
    <p class="label__type">Prosecco</p>
    <p class="label__region">VENETO</p>
    <p class="label__igt">INDICAZIONE GEOGRAFICA TIPICA</p>
    <p class="label__style">FRIZZANTE</p>
  </article>

</main>
</body>
</html>
```